Postcard for Printing Company
LumaPress, Inc. New Ink Schedules / New PMS Rates
Project: Postcard for Printing Company
Postcard for Printing Company - Printing
Creative Brief
Printing
The postcard will target Print Brokers, Retail Printers, Print Shops, Graphic Designers and anyone in the printing industry.
We would like a small swatch/example next to each ink to display each color against its reference. The central theme of the post card is to promote our range of PMS inks and our ink schedule. Also, please include company logo on both the front and back of postcard. The postcard will target Print Brokers, Retail Printers, Print Shops, Graphic Designers and anyone in the printing industry. I would like the images to be used from BrivaleImages.com

```html
<!DOCTYPE html>
<html lang="en">
<head>
<meta charset="utf-8">
<title>LumaPress – Ink Effect Postcards</title>
<link rel="stylesheet" href="https://fonts.googleapis.com/css2?family=Special+Elite&family=Open+Sans:wght@600;700&display=swap">
<style>
  :root {
    --stage: #c9c9c9;
    --card: #ffffff;
    --ink-black: #111111;
    --brand-red: #c4262e;
    --brand-dark: #333333;
    --beige: #d9c6a3;
    --orange: #e8612c;
    --teal: #1a8a9a;
    --blue: #2a57a0;
    --violet: #4a3a8c;
    --sand: #d8c2a2;
    --lime: #c9dc8a;
    --mint: #5cc08a;
    --olive: #9ab83a;
    --moss: #6f9a3a;
  }
  * { margin: 0; padding: 0; box-sizing: border-box; }
  html, body { width: 1200px; height: 961px; overflow: hidden; background: var(--stage); }
  .stage { position: relative; width: 1200px; height: 961px; }
  .postcard {
    position: absolute; top: 57px; width: 561px; height: 839px;
    background: var(--card);
    box-shadow: 2px 3px 6px rgba(0,0,0,.25);
  }
  .postcard--warm { left: 31px; }
  .postcard--fresh { left: 623px; }

  .swatches { position: absolute; top: 143px; left: 146px; display: flex; gap: 13px; }
  .swatch { width: 36px; height: 36px; }

  .ink-art {
    position: absolute; top: 213px; left: 47px; width: 473px; height: 488px;
  }
  .postcard--warm .ink-art {
    background:
      radial-gradient(circle at 20% 30%, rgba(26,138,154,.8), transparent 45%),
      radial-gradient(circle at 80% 70%, rgba(42,87,160,.85), transparent 50%),
      radial-gradient(circle at 50% 50%, rgba(17,17,17,.75), transparent 60%),
      linear-gradient(135deg, var(--orange), var(--violet) 45%, var(--teal) 75%, var(--beige));
  }
  .postcard--fresh .ink-art {
    background:
      radial-gradient(circle at 25% 35%, rgba(92,192,138,.8), transparent 45%),
      radial-gradient(circle at 75% 65%, rgba(154,184,58,.85), transparent 50%),
      radial-gradient(circle at 50% 50%, rgba(17,17,17,.7), transparent 60%),
      linear-gradient(135deg, var(--lime), var(--moss) 45%, var(--mint) 75%, var(--sand));
  }
  .ink-letters {
    position: absolute; inset: 30px 40px;
    display: grid; grid-template-columns: repeat(3, 1fr); grid-template-rows: repeat(3, 1fr);
    place-items: center;
    font-family: "Special Elite", "Courier New", monospace;
    font-size: 128px; line-height: 1; color: #fff;
  }
  .ink-letters span {
    display: flex; align-items: center; justify-content: center;
    width: 118px; height: 118px; background: rgba(10,10,10,.82); border-radius: 12px;
  }

  .brand { position: absolute; top: 742px; left: 0; width: 100%; text-align: center; }
  .brand-line { display: inline-flex; align-items: center; gap: 14px; }
  .brand-mark { width: 40px; height: 40px; background: var(--brand-dark); }
  .brand-name {
    font-family: "Open Sans", Arial, sans-serif; font-weight: 700;
    font-size: 44px; letter-spacing: -1px; color: var(--brand-red);
  }
  .brand-services {
    margin-top: 6px;
    font-family: "Open Sans", Arial, sans-serif; font-weight: 600;
    font-size: 13px; letter-spacing: 4px; color: var(--brand-dark);
  }
</style>
</head>
<body>
<main class="stage">
  <article class="postcard postcard--warm">
    <div class="swatches">
      <div class="swatch" style="background:var(--beige)"></div>
      <div class="swatch" style="background:var(--orange)"></div>
      <div class="swatch" style="background:var(--teal)"></div>
      <div class="swatch" style="background:var(--blue)"></div>
      <div class="swatch" style="background:var(--ink-black)"></div>
    </div>
    <div class="ink-art" role="img" aria-label="Halftone ink texture in orange, blue, teal and beige">
      <div class="ink-letters"><span>i</span><span>n</span><span>k</span><span>e</span><span>f</span><span>f</span><span>e</span><span>c</span><span>t</span></div>
    </div>
    <div class="brand">
      <div class="brand-line"><div class="brand-mark"></div><div class="brand-name">LumaPress</div></div>
      <div class="brand-services">THERMOGRAPHY | OFFSET | DIGITAL</div>
    </div>
  </article>

  <article class="postcard postcard--fresh">
    <div class="swatches">
      <div class="swatch" style="background:var(--sand)"></div>
      <div class="swatch" style="background:var(--lime)"></div>
      <div class="swatch" style="background:var(--mint)"></div>
      <div class="swatch" style="background:var(--olive)"></div>
      <div class="swatch" style="background:var(--ink-black)"></div>
    </div>
    <div class="ink-art" role="img" aria-label="Halftone ink texture in greens, olive and sand">
      <div class="ink-letters"><span>i</span><span>n</span><span>k</span><span>e</span><span>f</span><span>f</span><span>e</span><span>c</span><span>t</span></div>
    </div>
    <div class="brand">
      <div class="brand-line"><div class="brand-mark"></div><div class="brand-name">LumaPress</div></div>
      <div class="brand-services">THERMOGRAPHY | OFFSET | DIGITAL</div>
    </div>
  </article>
</main>
</body>
</html>
```